Original catchy book cover

I need a book cover for my book "The Steady Harbor Manual" (https://quillpress.example/harbormanual). This will be a book self published on brightmart.
The book talks about the following concepts:
- Iterative product delivery
- Early discovery using feedback from customers
- Start small, think big, move fast
- Slice the product into valuable increments that can be validated with customers
- Experimental approach to deciding the next slice of work
A simple cover that stands out from the business books already out there! Some examples are:
https://www.brightmart.example/Field-Notes-Thriving-Teams-Steadily-ebook/dp/Q00XTR4KWZ/ref=sr_1_1?ie=UTF8&qid=1500000001&sr=8-1&keywords=field+notes
https://www.brightmart.example/Quiet-Harbor-Almanac-Shape-Offerings-ebook/dp/Q00MVK219J/ref=sr_1_1?s=digital-text&ie=UTF8&qid=1500000002&sr=1-1&keywords=quiet+harbor+almanac
https://www.brightmart.example/Course-Charts-Renewed-Heading-Fog-ebook/dp/Q099WT71ZD/ref=pd_sim_351_2?_encoding=UTF8&psc=1&refRID=9QZTRWJDDAV52LM0NKPP
Lastly, attached are 2 draft covers that i've been playing with. Would love a graphic as part of the cover if it makes sense in your design! The graphic should tie to the meaning or themes of the book. Emphasis on ways of working, collaboration, experimentation, hypothesis, agile, incremental or adaptive. Those are some words that describe the content of the book.
Alternatively, something abstract could also be an option if a literal graphic doesn't suit the theme of your design.
Target Market(s)
Product owners, scrum masters, people in the agile community, software developers, designers
Industry/Entity Type
Information Technology
Font styles to use
Colors
Designer to choose colors to be used in the design.
Requirements
Must have
- Title, Subtitle, Author Name
- Back of the book should have space for a description (use lorem ipsum for now)
- Please use the editorial logo
- (please omit "created by Tomas Verlindt" because the editorial logo replaces that.
- The design must be original art or graphics (i.e. it should be similar to another cover in this topic).
Nice to have
- A graphic would be ideal if it is relevant to the book topic, otherwise a nice simple cover that uses colors or patterns that are easy to recall.
- The color suggestions below are suggestions only. Do not feel you have to incorporate all the colors and feel free to recommend an alternate palette.
Should not have
- Clipart or generic stock art photos. Images for the sake of images, traditional logos (e.g. a computer, a phone etc unless it's part of an overall theme that ties the logos together).

```html
<!DOCTYPE html>
<html lang="en">
<head>
<meta charset="utf-8">
<title>The Steady Harbor Manual — Book Cover</title>
<link href="https://fonts.googleapis.com/css2?family=Jost:wght@300;800&display=swap" rel="stylesheet">
<style>
  :root {
    --page: #ffffff;
    --red: #e8262b;
    --green: #8fc63e;
    --yellow: #fbb917;
    --ink-white: #ffffff;
    --ink-green: #1c7a3e;
  }
  html, body {
    margin: 0;
    width: 1200px;
    height: 1200px;
    overflow: hidden;
    background: var(--page);
  }
  .cover-art {
    position: absolute;
    left: 270px;
    top: 90px;
    width: 660px;
    height: 1020px;
    background: linear-gradient(165deg,
      var(--green) 0%,
      var(--red) 22%,
      var(--red) 68%,
      var(--green) 84%,
      var(--yellow) 100%);
  }
  .cover-type {
    position: absolute;
    left: 0;
    top: 0;
    width: 1200px;
    height: 1200px;
  }
  .title-light { font-family: "Jost", sans-serif; font-weight: 300; fill: var(--ink-white); font-size: 96px; }
  .title-heavy { font-family: "Jost", sans-serif; font-weight: 800; fill: var(--ink-white); }
  .subtitle { font-family: "Jost", sans-serif; font-weight: 300; fill: var(--ink-white); font-size: 32px; }
  .author { font-family: "Jost", sans-serif; font-weight: 300; fill: var(--ink-green); font-size: 46px; }
</style>
</head>
<body>
  <div class="cover-art" role="img" aria-label="Abstract artwork of overlapping red, green, blue and yellow geometric shapes"></div>

  <svg class="cover-type" viewBox="0 0 1200 1200" xmlns="http://www.w3.org/2000/svg" aria-label="The Steady Harbor Manual, a practitioner's guide, by Mara Quell">
    <text class="title-light" x="575" y="420" text-anchor="middle">THE STEADY</text>
    <text class="title-heavy" x="580" y="540" text-anchor="middle" font-size="112">HARBOR</text>
    <text class="title-heavy" x="580" y="652" text-anchor="middle" font-size="118">MANUAL</text>

    <text class="subtitle" x="617" y="728" text-anchor="middle">A PRACTITIONER’S GUIDE</text>
    <text class="subtitle" x="617" y="768" text-anchor="middle">TO BUILDING VIABLE PRODUCTS</text>
    <text class="subtitle" x="617" y="807" text-anchor="middle">CUSTOMERS LOVE.</text>

    <text class="author" x="874" y="1068" text-anchor="end">Mara Quell</text>
  </svg>
</body>
</html>
```